We are an integrated facilities management company.

We aggregate everything related to facilities maintenance. Repair-replacement of equipment and facility space materials from:
Asset gathering and tracking.
Vendor screening, contracting and management.
Service requirement development.
Work order processing and management.
Invoice reconciliation.
Vendor payment.
Reporting.
Capital equipment bids and project management.

Target Market(s)

Retail, hospitality, multi-family housing, long term healthcare.

Industry/Entity Type

Maintenance

Contact Information for Business Card

Professional and bold look. (see logo zip file)

Colors
3377b5
85abd2
cedeed

Requirements
Must have
• N/A
Nice to have
• N/A
Should not have
• N/A

```html
<!DOCTYPE html>
<html lang="en">
<head>
<meta charset="utf-8">
<title>Meridian Facility Partners – Business Card</title>
<link href="https://fonts.googleapis.com/css2?family=Montserrat:wght@600;700&family=Open+Sans:wght@400;600&display=swap" rel="stylesheet">
<style>
  :root{
    --bg:#3a3a3c;
    --card:#2b2c2e;
    --card-deep:#1d1e20;
    --blue:#3377b5;
    --blue-light:#85abd2;
    --blue-pale:#cedeed;
    --grey:#8e9093;
    --grey-dark:#5d5f62;
    --white:#f2f2f2;
  }
  *{margin:0;padding:0;box-sizing:border-box}
  html,body{width:1200px;height:1021px;overflow:hidden;background:var(--bg)}
  .canvas{position:relative;width:1200px;height:1021px}
  .card{position:absolute;left:280px;width:640px;height:366px;border-radius:4px;
        box-shadow:0 14px 30px rgba(0,0,0,.45);overflow:hidden}
  .card--front{top:70px;background:var(--card-deep)}
  .card--back{top:540px;background:var(--card)}
  .pattern{position:absolute;inset:0}
  .brand{position:absolute;text-align:left}
  .card--front .brand{left:150px;top:128px}
  .card--back .brand{left:150px;top:46px}
  .brand__row{display:flex;align-items:center;gap:14px}
  .brand__mark{width:54px;height:54px;background:var(--blue)}
  .brand__name{font-family:"Montserrat",sans-serif;font-weight:700;color:var(--blue-light);
        font-size:30px;line-height:1.05;letter-spacing:.5px;text-transform:uppercase}
  .brand__tagline{font-family:"Montserrat",sans-serif;font-weight:600;color:var(--grey);
        font-size:11px;letter-spacing:4px;margin-top:10px;margin-left:68px}
  .person{position:absolute;right:360px;top:212px;text-align:right;font-family:"Open Sans",sans-serif}
  .person__name{color:var(--blue);font-weight:600;font-size:21px;letter-spacing:.5px;text-transform:uppercase}
  .person__title{color:var(--white);font-size:15px;letter-spacing:.5px;margin-top:4px}
  .divider{position:absolute;left:300px;top:200px;width:1px;height:120px;background:var(--grey-dark)}
  .contact{position:absolute;left:322px;top:200px;font-family:"Open Sans",sans-serif;
        color:var(--white);font-size:15px;line-height:1.45}
  .contact__address{margin-bottom:4px}
  .contact__line{display:flex;align-items:center;gap:9px}
  .contact__line svg{width:14px;height:14px;flex:none}
</style>
</head>
<body>
<main class="canvas">

  <section class="card card--front">
    <svg class="pattern" role="img" aria-label="Repeating company monogram pattern in grey and black" width="640" height="366">
      <defs>
        <linearGradient id="patternFade" x1="0" y1="0" x2="1" y2="1">
          <stop offset="0" stop-color="#6a6b6e"/>
          <stop offset=".45" stop-color="#2f3033"/>
          <stop offset="1" stop-color="#141517"/>
        </linearGradient>
      </defs>
      <rect width="640" height="366" fill="url(#patternFade)"/>
    </svg>
    <div class="brand">
      <div class="brand__row">
        <span class="brand__mark"></span>
        <span class="brand__name">Meridian<br>Facility Partners</span>
      </div>
      <div class="brand__tagline">MAINTAIN • REPAIR • REPLACE</div>
    </div>
  </section>

  <section class="card card--back">
    <div class="brand">
      <div class="brand__row">
        <span class="brand__mark"></span>
        <span class="brand__name">Meridian<br>Facility Partners</span>
      </div>
      <div class="brand__tagline">MAINTAIN • REPAIR • REPLACE</div>
    </div>

    <div class="person">
      <div class="person__name">Daniel Reyes</div>
      <div class="person__title">FOUNDER</div>
    </div>

    <div class="divider"></div>

    <div class="contact">
      <div class="contact__address">480 Harbor Point Drive, Suite 310<br>Tampa, Florida, 33602</div>
      <div class="contact__line">
        <svg viewBox="0 0 24 24"><path fill="#3377b5" d="M6.6 10.8a15 15 0 0 0 6.6 6.6l2.2-2.2a1 1 0 0 1 1-.25 11.4 11.4 0 0 0 3.6.57 1 1 0 0 1 1 1V20a1 1 0 0 1-1 1A17 17 0 0 1 3 4a1 1 0 0 1 1-1h3.5a1 1 0 0 1 1 1c0 1.25.2 2.45.57 3.6a1 1 0 0 1-.25 1z"/></svg>
        (555) 214-6630
      </div>
      <div class="contact__line">
        <svg viewBox="0 0 24 24"><rect x="2" y="5" width="20" height="14" fill="none" stroke="#3377b5" stroke-width="2"/><path d="M2 5l10 8 10-8" fill="none" stroke="#3377b5" stroke-width="2"/></svg>
        daniel@meridianfacility.com
      </div>
      <div class="contact__line">
        <svg viewBox="0 0 24 24"><circle cx="12" cy="12" r="9.5" fill="none" stroke="#3377b5" stroke-width="2"/><path d="M2.5 12h19M12 2.5c3 3 3 16 0 19M12 2.5c-3 3-3 16 0 19" fill="none" stroke="#3377b5" stroke-width="1.6"/></svg>
        www.meridianfacility.com
      </div>
    </div>
  </section>

</main>
</body>
</html>
```